I'm doing a recreational cannabis grow business here in the Columbia Gorge scenic area . I'm looking for a business card similar to the Tarvelle Lodge logo,except for the sun raise to be pot leafs.
The Gorge mountains,the river with the sun coming off the water between the mountains with the pot leaf rays.
All print would be on the back side
Kick ass simple black and gold or kick ass colorful

Target Market(s)

Retailers

Industry/Entity Type

Business

Contact Information for Business Card

Lofty Fern
In the heart of the Columbia River Gorge
Email loftyfernllc@pinemail.net

Font styles to use
Other font styles liked:
• What the artist thinks

Colors

Designer to choose colors to be used in the design.

Requirements
Must have
• Nice to look at . Like that bottle of wine you buy because the label graphics told you too.
Nice to have
• It's in my description
• You can lookup the Tarvelle Logde in Stevenson Wa and check out there logo, and I'm always up for ideas.
• Color and fonts should be what the artist thinks best
Should not have
• Boring

```html
<!DOCTYPE html>
<html lang="en">
<head>
<meta charset="utf-8">
<title>Lofty Fern Business Card</title>
<link href="https://fonts.googleapis.com/css2?family=Open+Sans:wght@400;600;700&display=swap" rel="stylesheet">
<style>
  :root{
    --stage:#2e2e2e;
    --card:#ffffff;
    --ink:#111111;
    --text:#222222;
    --accent-blue:#1e8fd1;
    --olive:#6b7a52;
    --mark-green:#4f6b3c;
    --faint-mark:#f4f3ef;
  }
  *{margin:0;padding:0;box-sizing:border-box}
  html,body{width:1200px;height:880px;overflow:hidden}
  body{background:var(--stage);position:relative;font-family:"Open Sans",Arial,sans-serif;color:var(--text)}
  .card{position:absolute;width:620px;height:354px;background:var(--card);border-radius:24px;overflow:hidden}
  .card-front{left:60px;top:60px}
  .card-back{left:520px;top:466px}
  .faint-mark{position:absolute;border-radius:50%;background:var(--faint-mark)}
  .card-front .faint-mark{width:360px;height:360px;left:160px;top:20px}
  .card-back .faint-mark{width:230px;height:230px;right:30px;top:-70px}
  .wordmark{position:absolute;display:flex;align-items:center;gap:14px}
  .wordmark-dot{width:44px;height:44px;border-radius:50%;background:var(--mark-green)}
  .wordmark-name{font-weight:700;color:var(--ink);letter-spacing:.5px;white-space:nowrap}
  .card-front .wordmark{left:50%;top:50%;transform:translate(-50%,-50%)}
  .card-front .wordmark-name{font-size:42px}
  .card-back .wordmark{left:44px;top:88px}
  .card-back .wordmark-name{font-size:42px}
  .person{position:absolute;right:44px;top:138px;text-align:right}
  .person-name{font-weight:700;font-size:20px;line-height:26px;color:var(--accent-blue);letter-spacing:.5px}
  .person-title{font-size:14px;line-height:20px;color:var(--text)}
  .divider{position:absolute;left:44px;right:44px;top:200px;height:1px;background:var(--olive)}
  .contact-list{position:absolute;left:44px;top:234px;list-style:none}
  .contact-list li{display:flex;align-items:center;gap:8px;font-size:15px;line-height:24px;white-space:nowrap}
  .contact-icon{width:18px;height:18px;border-radius:4px;background:var(--accent-blue);display:flex;align-items:center;justify-content:center;flex:none}
  .tagline{position:absolute;right:44px;top:240px;text-align:right;font-size:15px;line-height:22px;font-style:normal}
</style>
</head>
<body>
  <section class="card card-front" aria-label="Card front">
    <div class="faint-mark"></div>
    <div class="wordmark">
      <span class="wordmark-dot"></span>
      <span class="wordmark-name">Lofty Fern</span>
    </div>
  </section>

  <section class="card card-back" aria-label="Card back">
    <div class="faint-mark"></div>
    <div class="wordmark">
      <span class="wordmark-dot"></span>
      <span class="wordmark-name">Lofty Fern</span>
    </div>
    <div class="person">
      <p class="person-name">OWEN HALE</p>
      <p class="person-title">Managing Director</p>
    </div>
    <div class="divider"></div>
    <ul class="contact-list">
      <li><span class="contact-icon"><svg width="12" height="12" viewBox="0 0 12 12"><path d="M3 1l2 2-1 1.5c.6 1.4 1.6 2.4 3 3L8.5 6.5l2 2L9 10.5C5 10 2 7 1.5 3z" fill="#fff"/></svg></span>(01) 5550 4417</li>
      <li><span class="contact-icon"><svg width="12" height="12" viewBox="0 0 12 12"><rect x="1" y="3" width="10" height="7" fill="none" stroke="#fff" stroke-width="1.2"/><path d="M1 3l5 4 5-4" fill="none" stroke="#fff" stroke-width="1.2"/></svg></span>loftyfernllc@pinemail.net</li>
      <li><span class="contact-icon"><svg width="12" height="12" viewBox="0 0 12 12"><circle cx="6" cy="6" r="4.5" fill="none" stroke="#fff" stroke-width="1.1"/><ellipse cx="6" cy="6" rx="2" ry="4.5" fill="none" stroke="#fff" stroke-width="1"/><path d="M1.5 6h9" stroke="#fff" stroke-width="1"/></svg></span>www.loftyfern.net</li>
    </ul>
    <p class="tagline">In the heart of the<br>Columbia River Gorge</p>
  </section>
</body>
</html>
```